Coach company requires modern brochure

We need a brochure designed that shows our various coach services. The aim of the brochure is to attract new business, therefore we need something that is modern, eye-catching and uses a lot of imagery/design rather than being text heavy.

I have all the images that can be sent via dropbox or google drive if you want to request them.

Target Market(s)

Wedding planners, event companies, school business managers, sporting groups

Industry/Entity Type

Tourism

Requirements
Must have
• 4 x a4 pages
• Bold and eye catching cover page

```html
<!DOCTYPE html>
<html lang="en">
<head>
<meta charset="utf-8">
<title>Shoreline Coaches – Brochure</title>
<link rel="stylesheet" href="https://fonts.googleapis.com/css2?family=Open+Sans:wght@400;600;700&family=Dancing+Script:wght@500&display=swap">
<style>
  :root{
    --stage:#e6e6e6;
    --paper:#ffffff;
    --paper-shade:#ececec;
    --green:#3ba843;
    --green-dark:#2c9a48;
    --sky:#8ec6ea;
    --blue:#3aa2dc;
    --orange:#f0883a;
    --ink:#444a50;
    --muted:#7a8187;
  }
  *{box-sizing:border-box;margin:0;padding:0}
  html,body{width:1049px;height:1200px;overflow:hidden;background:var(--stage)}
  body{font-family:"Open Sans",Arial,sans-serif;color:var(--ink);position:relative}
  .spread{position:absolute;left:44px;width:960px;height:430px;background:
      linear-gradient(90deg,var(--paper) 0%,var(--paper) 40%,var(--paper-shade) 50%,var(--paper) 60%,var(--paper) 100%);
      box-shadow:0 6px 18px rgba(0,0,0,.18);overflow:hidden}
  .spread--outer{top:120px}
  .spread--inner{top:660px}
  .spread__art{position:absolute;inset:0;width:960px;height:430px}
  .tile{stroke:#fff;stroke-width:5}
  .block{position:absolute;z-index:1}

  /* wordmark */
  .wordmark{display:flex;align-items:center;gap:8px;color:var(--green);font-weight:600;letter-spacing:.2px;white-space:nowrap}
  .wordmark__dot{width:14px;height:14px;border-radius:50%;background:var(--green)}
  .wordmark--small{font-size:17px}
  .wordmark--large{font-size:20px}
  .wordmark--large .wordmark__dot{width:16px;height:16px}

  /* back cover contact */
  .contact{left:262px;top:150px;width:210px}
  .contact__title{font-size:10px;font-weight:700;margin:18px 0 4px}
  .contact__phone{font-size:15px;color:var(--ink);margin-bottom:3px}
  .contact__line{font-size:8.5px;color:var(--muted);line-height:1.5}
  .contact__social{display:flex;align-items:center;gap:5px;font-size:8.5px;color:var(--muted);margin-top:5px}
  .contact__icon{width:9px;height:9px;border-radius:50%;background:var(--blue)}
  .contact__social + .contact__social{margin-top:3px}
  .contact__social:first-of-type{margin-top:14px}

  /* front cover */
  .cover-mark{left:548px;top:52px}
  .tagline{left:560px;top:100px;font-family:"Dancing Script",cursive;color:var(--green-dark);font-size:30px;line-height:1.15;white-space:nowrap}
  .tagline span{display:block;padding-left:30px}
  .cover-web{right:18px;bottom:8px;font-size:7px;color:var(--muted);white-space:nowrap}

  /* inner pages */
  .section h2{font-size:12px;font-weight:700;margin-bottom:4px}
  .section p{font-size:8.5px;line-height:1.5;color:var(--muted)}
  .section--blue h2{color:var(--blue)}
  .section--green h2{color:var(--green)}
  .about{left:245px;top:28px;width:215px}
  .weddings{left:240px;top:122px;width:220px}
  .events{left:140px;top:238px;width:220px}
  .educational{left:515px;top:140px;width:210px}
  .sporting{left:510px;top:230px;width:160px}
  .note{border:1.5px solid var(--orange);border-radius:5px;padding:6px 9px;font-size:8.5px;line-height:1.45;color:var(--orange)}
  .note--left{left:140px;top:345px;width:200px}
  .note--right{left:515px;top:34px;width:270px}
  .note-sub{left:520px;top:86px;font-size:7.5px;color:var(--muted)}
  .closing{left:510px;top:312px;width:150px;font-size:8.5px;line-height:1.5;color:var(--muted)}
  .closing strong{color:var(--blue);font-weight:700;font-size:10px}
</style>
</head>
<body>

<section class="spread spread--outer" aria-label="Brochure outer spread">
  <svg class="spread__art" viewBox="0 0 960 430">
    <defs>
      <linearGradient id="g-road" x1="0" y1="0" x2="0" y2="1"><stop offset="0" stop-color="#b9c9c4"/><stop offset=".5" stop-color="#6f8a5e"/><stop offset="1" stop-color="#7b7b74"/></linearGradient>
      <linearGradient id="g-building" x1="0" y1="0" x2="0" y2="1"><stop offset="0" stop-color="#d98a6c"/><stop offset=".55" stop-color="#6a4a3e"/><stop offset="1" stop-color="#2e3a3f"/></linearGradient>
      <linearGradient id="g-stadium" x1="0" y1="0" x2="0" y2="1"><stop offset="0" stop-color="#8a8f97"/><stop offset=".5" stop-color="#4e8a3a"/><stop offset="1" stop-color="#3c7a2e"/></linearGradient>
      <linearGradient id="g-coach" x1="0" y1="0" x2="0" y2="1"><stop offset="0" stop-color="#cfe3f2"/><stop offset=".55" stop-color="#f4f4f4"/><stop offset="1" stop-color="#7d8a7e"/></linearGradient>
      <linearGradient id="g-beach" x1="0" y1="0" x2="0" y2="1"><stop offset="0" stop-color="#d3dbe3"/><stop offset=".55" stop-color="#9fb0bb"/><stop offset="1" stop-color="#5f7a53"/></linearGradient>
    </defs>
    <!-- back cover -->
    <polygon class="tile" fill="var(--sky)" points="60,-75 135,0 60,75 -15,0"/>
    <polygon class="tile" fill="var(--green)" points="258,-36 316,22 258,80 200,22"/>
    <polygon class="tile" fill="url(#g-road)" points="160,18 242,100 160,182 78,100" role="img" aria-label="Photo: tree-lined country road"/>
    <polygon class="tile" fill="var(--green)" points="12,95 67,150 12,205 -43,150"/>
    <polygon class="tile" fill="url(#g-building)" points="92,170 184,262 92,354 0,262" role="img" aria-label="Photo: coastal hotel building at dusk"/>
    <polygon class="tile" fill="var(--sky)" points="0,325 55,380 0,435 -55,380"/>
    <polygon class="tile" fill="var(--sky)" points="150,380 200,430 150,480 100,430"/>
    <circle cx="215" cy="300" r="34" fill="#e3f1fa" stroke="var(--sky)" stroke-width="3"/>
    <!-- front cover -->
    <polygon class="tile" fill="var(--sky)" points="630,-40 670,0 630,40 590,0"/>
    <polygon class="tile" fill="url(#g-stadium)" points="875,-15 960,70 875,155 790,70" role="img" aria-label="Photo: sports stadium with green field"/>
    <polygon class="tile" fill="url(#g-coach)" points="900,150 975,225 900,300 825,225" role="img" aria-label="Photo: white touring coach parked"/>
    <polygon class="tile" fill="url(#g-beach)" points="730,195 810,275 730,355 650,275" role="img" aria-label="Photo: beach with pandanus tree"/>
    <polygon class="tile" fill="var(--green)" points="960,290 1020,350 960,410 900,350"/>
    <polygon class="tile" fill="var(--sky)" points="860,395 900,435 860,475 820,435"/>
    <polygon class="tile" fill="var(--green)" points="650,345 735,430 650,515 565,430"/>
    <polygon class="tile" fill="var(--green-dark)" points="770,390 810,430 770,470 730,430"/>
  </svg>

  <div class="block contact">
    <div class="wordmark wordmark--small"><span class="wordmark__dot"></span>Shoreline Coaches</div>
    <p class="contact__title">Contact Us</p>
    <p class="contact__phone">1300 482 615</p>
    <p class="contact__line">info@shorelinecoaches.com.au</p>
    <p class="contact__line">www.shorelinecoaches.com.au</p>
    <p class="contact__social"><span class="contact__icon"></span>@ShorelineCoachesBus</p>
    <p class="contact__social"><span class="contact__icon"></span>@shoreline_coaches</p>
  </div>

  <div class="block cover-mark"><div class="wordmark wordmark--large"><span class="wordmark__dot"></span>Shoreline Coaches</div></div>
  <p class="block tagline">Connecting<span>the Coast....</span></p>
  <p class="block cover-web">www.shorelinecoaches.com.au</p>
</section>

<section class="spread spread--inner" aria-label="Brochure inner spread">
  <svg class="spread__art" viewBox="0 0 960 430">
    <defs>
      <linearGradient id="g-office" x1="0" y1="0" x2="0" y2="1"><stop offset="0" stop-color="#9fb4c8"/><stop offset="1" stop-color="#4b5e74"/></linearGradient>
      <linearGradient id="g-hotel" x1="0" y1="0" x2="0" y2="1"><stop offset="0" stop-color="#e8ecef"/><stop offset="1" stop-color="#7fb7a6"/></linearGradient>
      <linearGradient id="g-interior" x1="0" y1="0" x2="0" y2="1"><stop offset="0" stop-color="#c9ced3"/><stop offset="1" stop-color="#4d555c"/></linearGradient>
      <linearGradient id="g-team" x1="0" y1="0" x2="0" y2="1"><stop offset="0" stop-color="#7aa8c9"/><stop offset=".6" stop-color="#3f7fb3"/><stop offset="1" stop-color="#2c4b63"/></linearGradient>
      <linearGradient id="g-palm" x1="0" y1="0" x2="0" y2="1"><stop offset="0" stop-color="#bcd8ec"/><stop offset="1" stop-color="#4f7a45"/></linearGradient>
      <linearGradient id="g-pool" x1="0" y1="0" x2="0" y2="1"><stop offset="0" stop-color="#4fb0e0"/><stop offset="1" stop-color="#1f6fa8"/></linearGradient>
    </defs>
    <!-- left page -->
    <polygon class="tile" fill="var(--green)" points="60,-55 115,0 60,55 5,0"/>
    <polygon class="tile" fill="url(#g-office)" points="160,-10 230,60 160,130 90,60" role="img" aria-label="Photo: staff planning bookings"/>
    <polygon class="tile" fill="var(--sky)" points="35,65 80,110 35,155 -10,110"/>
    <polygon class="tile" fill="url(#g-hotel)" points="105,103 167,165 105,227 43,165" role="img" aria-label="Photo: wedding table setting"/>
    <polygon class="tile" fill="url(#g-interior)" points="55,195 120,260 55,325 -10,260" role="img" aria-label="Photo: coach interior seating"/>
    <polygon class="tile" fill="var(--green)" points="10,320 70,380 10,440 -50,380"/>
    <polygon class="tile" fill="var(--sky)" points="110,385 155,430 110,475 65,430"/>
    <!-- right page -->
    <polygon class="tile" fill="var(--green)" points="720,205 765,250 720,295 675,250"/>
    <polygon class="tile" fill="url(#g-palm)" points="860,170 930,240 860,310 790,240" role="img" aria-label="Photo: palm trees against the sky"/>
    <polygon class="tile" fill="var(--green-dark)" points="960,125 1015,180 960,235 905,180"/>
    <polygon class="tile" fill="url(#g-team)" points="740,275 810,345 740,415 670,345" role="img" aria-label="Photo: school group in uniform"/>
    <polygon class="tile" fill="url(#g-pool)" points="870,308 932,370 870,432 808,370" role="img" aria-label="Photo: swimmer in a pool"/>
    <polygon class="tile" fill="var(--sky)" points="960,385 1005,430 960,475 915,430"/>
    <polygon class="tile" fill="var(--green)" points="620,385 665,430 620,475 575,430"/>
  </svg>

  <div class="block section section--green about">
    <h2>About Us</h2>
    <p>We are a family-run coach operator serving the coast and hinterland. Our modern fleet and friendly drivers get your group where it needs to be, safely, comfortably and on time.</p>
  </div>
  <div class="block section section--blue weddings">
    <h2>Weddings &amp; Events</h2>
    <p>Make your big day effortless. We transfer guests between ceremony, reception and accommodation, with a clean, air-conditioned coach and a driver dressed for the occasion.</p>
  </div>
  <div class="block section section--green events">
    <h2>Events</h2>
    <p>Festivals, conferences, concerts and corporate days. We plan routes, pick-up points and timing so your delegates arrive relaxed and ready.</p>
  </div>
  <p class="block note note--left">Ask about our package rates for return transfers.</p>

  <p class="block note note--right">All our coaches are fully accredited, seat-belted and maintained to the highest safety standards.</p>
  <p class="block note-sub">Bookings essential during school holidays.</p>
  <div class="block section section--blue educational">
    <h2>Educational Groups</h2>
    <p>Excursions, camps, carnivals and sports days. Our accredited drivers hold current blue cards and know the local schools, venues and routes well.</p>
  </div>
  <div class="block section section--green sporting">
    <h2>Sporting Groups</h2>
    <p>From weekend fixtures to interstate tournaments, we move teams, coaches and gear with plenty of room for kit bags.</p>
  </div>
  <p class="block closing">For your full range of service needs we would love to discuss your enquiry. Please call <strong>1300 482 615</strong></p>
</section>

</body>
</html>
```